Fresh and unique Mortgage Broking business needs website design.

We need a professional yet fresh, bright and colourful website for my Mortgage broking business.
We specialise in the Non conforming/sub prime market with clients who have been rejected by other banks or have trouble getting finance through a traditional lender.
We are called Brightwell Lending and we aim to provide Hope to our clients when they have thought there was no hope.
I would like it to be on a Wordpress platform as I plan to do a lot of postings, both written and video and I need it to be easy to use.
I would also like it to be able to have a clear and simple enquiry box on the first page to capture contact details and notify me via email.

I have already had the logo designed in both green and black and a white version.
I have also had a a header made up using the white logo with leaves background that could possibly be used as the website header which I have used as my facebook header.

https://www.facebook.com/MarcusTolvenBright/

I tried playing around with a jimdo website builder which kind of got some of the brightness and colours I was after but it had a lot to go.

http://brightwelllending.sitevale.example/

Industry/Entity Type

Finance

Number of Pages Required

4 page

Colors
0292cd
00a990
fbed22
ffc214
f78f20
ec1f27

Requirements
Nice to have
• I'm not sure what the difference between uncoded and coded website is so I'm not sure what I need?

```html
<!DOCTYPE html>
<html lang="en">
<head>
<meta charset="utf-8">
<title>Brightwell Lending</title>
<link rel="stylesheet" href="https://fonts.googleapis.com/css2?family=Montserrat:wght@400;600;700&family=Open+Sans:wght@300;400;600;700&family=Raleway:wght@400;500&display=swap">
<style>
:root{
  --blue:#0292cd;
  --blue-bright:#1a9ad6;
  --navy:#111a2d;
  --navy-2:#172135;
  --slate:#2a3245;
  --ink:#1b1b1b;
  --text:#444;
  --muted:#9a9a9a;
  --white:#fff;
  --card-light:#f6f7f9;
}
*{box-sizing:border-box;margin:0;padding:0}
html,body{width:1200px;height:3035px;overflow:hidden}
body{font-family:"Open Sans",sans-serif;color:var(--text);background:var(--white);position:relative}
.abs{position:absolute}
section,header,footer{position:absolute;left:0;width:1200px;overflow:hidden}

/* top bar */
.topbar{top:0;height:40px;background:var(--blue-bright);color:var(--white);font-size:12.5px}
.topbar .abs{top:11px}
.region{top:10px!important;left:333px;background:var(--navy);padding:2px 8px;font-weight:700;font-size:11px;border-radius:2px}
.topbar svg{vertical-align:-2px;margin-right:6px}

/* header */
.masthead{top:40px;height:105px;background:var(--navy);color:var(--white)}
.brand{left:80px;top:34px;font-weight:600;font-size:25px;display:flex;align-items:center;gap:10px}
.brand i{width:14px;height:14px;border-radius:50%;background:var(--white);display:block}
.info{font-size:13px;font-weight:700;line-height:20px}
.social{left:998px;top:47px;display:flex;gap:24px}
.social span{width:12px;height:12px;border-radius:2px;background:var(--white);display:block}

/* hero */
.hero{top:145px;height:505px;background:
  linear-gradient(rgba(20,25,30,.28),rgba(20,25,30,.28)),
  linear-gradient(100deg,#5d6a70 0%,#8f969a 18%,#c9b29a 38%,#d8b48e 50%,#b79a7c 64%,#7d8b69 80%,#4f7a3e 100%)}
.hero h1{position:absolute;left:0;right:0;top:148px;text-align:center;font-weight:300;font-size:64px;line-height:82px;color:var(--white)}
.hero svg{position:absolute;top:222px}

/* welcome */
.welcome{top:650px;height:443px}
h2{font-family:"Montserrat",sans-serif;font-weight:700;color:var(--ink);font-size:35px}
h2 b{color:var(--blue)}
.rule{width:62px;height:3px;background:var(--blue)}
.welcome h2{position:absolute;left:80px;top:30px;font-family:"Open Sans",sans-serif;font-size:34px}
.welcome p{position:absolute;left:80px;top:114px;width:472px;font-size:15px;line-height:25.5px;color:#333}
.btn{position:absolute;background:var(--blue);color:var(--white);font-weight:700;text-align:center;font-size:14px}
.welcome .btn{left:80px;top:347px;width:155px;height:38px;line-height:38px}
.welcome .photo{left:613px;top:120px;width:508px;height:268px;background:linear-gradient(180deg,#f7f7f7 0%,#ededed 45%,#9fb3c9 68%,#4f6f97 85%,#e4e4e4 100%)}

/* cta band */
.cta{top:1093px;height:175px;background:var(--slate)}
.cta p{position:absolute;left:80px;top:73px;font-family:"Montserrat",sans-serif;font-weight:700;font-size:20px;color:var(--white)}
.cta .btn{left:963px;top:64px;width:157px;height:48px;line-height:48px;font-size:12.5px;font-weight:600}

/* services */
.services{top:1268px;height:502px}
.services h2{position:absolute;left:80px;top:28px;font-size:32px}
.services .rule{position:absolute;left:80px;top:88px}
.nav{position:absolute;top:36px;width:28px;height:28px;border:1px solid #cfcfcf;border-radius:50%}
.card{position:absolute;top:145px;width:330px}
.card .photo{height:195px}
.card h3{font-family:"Open Sans",sans-serif;font-weight:700;font-size:16px;color:var(--ink);margin-top:19px}
.card p{font-family:"Raleway",sans-serif;font-size:13px;line-height:24px;color:var(--muted);margin-top:6px}

/* call back */
.callback{top:1770px;height:367px;background:var(--navy)}
.callback .left{position:absolute;left:0;top:0;width:563px;height:367px;background:var(--navy-2)}
.callback h2{position:absolute;left:80px;top:62px;color:var(--white)}
.callback .rule{position:absolute;left:80px;top:128px}
.callback p{position:absolute;left:80px;width:440px;font-size:13.5px;line-height:22px;color:var(--white)}
.form-label{position:absolute;left:620px;top:68px;color:var(--white);font-weight:700;font-size:15px}
.field{position:absolute;width:248px;height:46px;background:var(--white);font-size:13px;color:#999;padding:13px 18px}
.callback .btn{left:620px;top:248px;width:523px;height:52px;line-height:52px;font-size:18px;font-weight:400}

/* testimonials */
.testimonials{top:2137px;height:558px}
.testimonials h2{position:absolute;left:80px;top:32px}
.testimonials .rule{position:absolute;left:80px;top:98px}
.dot{position:absolute;top:41px;width:14px;height:14px;border:2px solid var(--blue);border-radius:50%}
.dot.on{background:var(--blue)}
.quote{position:absolute;top:153px;width:330px;height:190px;padding:38px 40px 0 62px;font-size:14px;line-height:26px}
.quote.faded{background:var(--card-light);color:#cfd2d7}
.quote.active{background:var(--navy);color:var(--white)}
.quote svg{position:absolute;left:0;top:0}
.avatar{position:absolute;top:373px;width:64px;height:64px;border-radius:50%;background:linear-gradient(#eef0f2,#c3cad3)}
.person{position:absolute;top:455px;width:330px;text-align:center;font-family:"Montserrat",sans-serif;font-weight:700;font-size:16px}
.person span{font-family:"Open Sans",sans-serif;font-weight:400;font-size:13px;color:var(--blue)}
.person.faded{color:#b5b5b5}.person.faded span{color:#a8d6ec}
.stars{position:absolute;top:488px;width:330px;text-align:center;letter-spacing:4px;font-size:17px;color:var(--blue)}
.stars.faded{color:#a8d6ec}

/* footer */
.footer{top:2695px;height:290px;background:var(--navy);color:var(--white);font-size:13px}
.footer h4{position:absolute;top:42px;font-size:13px;font-weight:700}
.footer .abs{line-height:20px}
.links{left:395px;top:96px;line-height:34px!important}
.links .cur{color:var(--blue)}
.newsletter{left:615px;top:96px;width:240px;font-size:12px}
.footer input{position:absolute;left:615px;top:150px;width:225px;height:36px;border:0;padding:0 12px;font-family:"Open Sans",sans-serif;font-size:12.5px}
.footer .btn{left:615px;top:203px;width:225px;height:36px;line-height:36px;font-size:12px;font-weight:600}
.follow{left:922px;top:104px;display:flex;gap:21px}
.follow span{width:16px;height:16px;border-radius:3px;background:var(--white);display:block}
.follow span:first-child{background:var(--blue)}
.copyright{top:2985px;height:50px;background:#0b1220;color:var(--white);font-size:12.5px;text-align:center;line-height:50px}
</style>
</head>
<body>

<header class="topbar">
  <div class="abs" style="left:80px">Welcome to Brightwell Lending</div>
  <div class="abs region">USA ▾</div>
  <div class="abs" style="left:463px"><svg width="14" height="14" viewBox="0 0 24 24"><path fill="#fff" d="M6.6 10.8a15 15 0 0 0 6.6 6.6l2.2-2.2c.3-.3.7-.4 1-.2 1.1.4 2.3.6 3.6.6.6 0 1 .4 1 1V20c0 .6-.4 1-1 1A17 17 0 0 1 3 4c0-.6.4-1 1-1h3.5c.6 0 1 .4 1 1 0 1.3.2 2.5.6 3.6.1.3 0 .7-.2 1z"/></svg>CALL US: &nbsp;<b>+0400 555 182</b></div>
  <div class="abs" style="left:668px"><svg width="14" height="11" viewBox="0 0 24 18"><rect width="24" height="18" rx="2" fill="#fff"/><path d="M1 2l11 8 11-8" stroke="#1a9ad6" stroke-width="2" fill="none"/></svg>Mail US : <b>marcus@brightwelllending.example</b></div>
  <svg class="abs" style="left:1093px;top:9px" width="20" height="20" viewBox="0 0 24 24"><circle cx="10" cy="10" r="7" stroke="#fff" stroke-width="2.6" fill="none"/><path d="M15 15l6 6" stroke="#fff" stroke-width="3"/></svg>
</header>

<header class="masthead">
  <div class="abs brand"><i></i>Brightwell Lending</div>
  <svg class="abs" style="left:438px;top:34px" width="26" height="36" viewBox="0 0 26 36"><path d="M13 2a11 11 0 0 0-11 11c0 8 11 20 11 20s11-12 11-20A11 11 0 0 0 13 2z" stroke="var(--blue)" stroke-width="2.5" fill="none"/><circle cx="13" cy="13" r="4" fill="var(--blue)"/></svg>
  <div class="abs info" style="left:485px;top:34px">Lorem Ipsum Consectetur<br>Adipiscing</div>
  <svg class="abs" style="left:722px;top:34px" width="36" height="36" viewBox="0 0 36 36"><circle cx="18" cy="18" r="15" stroke="var(--blue)" stroke-width="2.5" fill="none"/><path d="M18 9v10h7" stroke="var(--blue)" stroke-width="2.5" fill="none"/></svg>
  <div class="abs info" style="left:772px;top:34px">Mon - Sat 9.00 - 20.00,<br>Sunday CLOSED</div>
  <div class="abs social" aria-label="Social links"><span></span><span></span><span></span><span></span></div>
</header>

<section class="hero" role="img" aria-label="Photo of a smiling family of four in front of their house">
  <h1>Lorem ipsum dolor<br>sectetur ipiscin</h1>
  <svg style="left:44px" width="40" height="66" viewBox="0 0 40 66"><path d="M34 4L8 33l26 29" stroke="#fff" stroke-width="8" fill="none" opacity=".85"/></svg>
  <svg style="left:1116px" width="40" height="66" viewBox="0 0 40 66"><path d="M6 4l26 29L6 62" stroke="var(--blue)" stroke-width="8" fill="none"/></svg>
</section>

<section class="welcome">
  <h2>Welcome to Brightwell Lending</h2>
  <p>Marcus lives in Pakenham and loves exploring the Cardinia Shire with his wife and kids for great places to eat.<br>With over 10 years' experience in financial services ranging from insurance, superannuation, investments and finance, Marcus bringing together his experience to provide a more holistic approach to his customers.<br>Marcus has a Diploma in Financial Planning, a Certificate IV in Finance and Mortgage Broking, and is a member of the NLBA</p>
  <div class="btn">READ MORE</div>
  <div class="abs photo" role="img" aria-label="Photo of a couple in denim sitting on the floor beside sketched furniture"></div>
</section>

<section class="cta">
  <p>Over 20 years of experience we'll ensure you always get the best guidance.</p>
  <div class="btn">RESQUEST QUOTE</div>
</section>

<section class="services">
  <h2>Services We Do</h2>
  <div class="rule"></div>
  <div class="nav" style="left:1048px"><svg width="26" height="26" viewBox="0 0 26 26"><path d="M15 8l-5 5 5 5" stroke="#777" stroke-width="1.6" fill="none"/></svg></div>
  <div class="nav" style="left:1091px"><svg width="26" height="26" viewBox="0 0 26 26"><path d="M11 8l5 5-5 5" stroke="#777" stroke-width="1.6" fill="none"/></svg></div>
  <div class="card" style="left:81px">
    <div class="photo" role="img" aria-label="Photo of a laptop and financial charts on a desk" style="background:linear-gradient(165deg,#ffffff 0%,#dfe4ea 35%,#8fa9c4 60%,#2f7fd0 85%,#1b5fae 100%)"></div>
    <h3>Debt consolidation</h3>
    <p>Market research vendors offering consulting services to advise on research methods used in developing and marketing products.</p>
  </div>
  <div class="card" style="left:437px">
    <div class="photo" role="img" aria-label="Photo of a magnifying glass over a blue bar chart" style="background:linear-gradient(170deg,#f1f1f1 0%,#cfd3d6 30%,#8e979e 48%,#6fa6de 70%,#2f86d6 100%)"></div>
    <h3>Investment loans</h3>
    <p>A merger means a combination of two companies to form a new company, while an acquisition is the purchase of one company</p>
  </div>
  <div class="card" style="left:791px">
    <div class="photo" role="img" aria-label="Photo of hands holding a tablet with a tree and city growing from it" style="background:linear-gradient(180deg,#e8ebea 0%,#b7c9a8 25%,#5f9a3c 50%,#4d7d34 65%,#8c969e 85%,#c9cdd1 100%)"></div>
    <h3>Residential loans</h3>
    <p>IT refers to "all processes of governing, whether undertaken by a government, market or network, whether over a family.</p>
  </div>
</section>

<section class="callback">
  <div class="left"></div>
  <h2>Request a call back<b>.</b></h2>
  <div class="rule"></div>
  <p style="top:152px">Lorem ipsum dolor sit amet, consectetur adipiscing elit. Ut placerat gravida magna, non tempor metus bibendum ac. Quisque sed lectus maximus Sed leo lorem, finibus vel lorem eu, facilisis consectetur urna.</p>
  <p style="top:262px">Duis ultrices bibendum magna, commodo interdum sem pretium sed. Aenean id est moada urna. Sed diam tellus, vehicula non tempus sit amet, iaculis hendrerit nisl.</p>
  <div class="form-label">I would like to discuss:</div>
  <div class="field" style="left:620px;top:103px">Turnaround Consulting<span style="position:absolute;right:16px;color:#666;font-size:9px;top:16px">▼</span></div>
  <div class="field" style="left:895px;top:103px">Your Name *</div>
  <div class="field" style="left:620px;top:175px">Your Mail *</div>
  <div class="field" style="left:895px;top:175px">Phone Number *</div>
  <div class="btn">SUBMIT</div>
</section>

<section class="testimonials">
  <h2>Testimonials<b>.</b></h2>
  <div class="rule"></div>
  <div class="dot" style="left:1052px"></div><div class="dot on" style="left:1079px"></div><div class="dot" style="left:1106px"></div>

  <div class="quote faded" style="left:80px"><svg width="60" height="40"><circle cx="27" cy="27" r="11" fill="none" stroke="#e4e6ea" stroke-width="2"/></svg>I can't thank them enough for how they helped My firm has been greatly helped by the excellent work from Broker, you won't be dis-appointed.</div>
  <div class="quote active" style="left:436px"><svg width="80" height="80"><path d="M0 0h80L0 80z" fill="var(--blue)"/><text x="16" y="36" fill="#fff" font-family="Georgia,serif" font-size="30" font-weight="700">“</text></svg>They have got my project on time with the competition with a highly skilled, well-organized and experienced team of professional Engineers.</div>
  <svg class="abs" style="left:589px;top:343px" width="24" height="14"><path d="M0 0h24L12 13z" fill="var(--navy)"/></svg>
  <div class="quote faded" style="left:790px"><svg width="60" height="40"><circle cx="27" cy="27" r="11" fill="none" stroke="#e4e6ea" stroke-width="2"/></svg>I can't thank them enough for how they helped My firm has been greatly helped by the excellent work from Broker, you won't be dis-appointed.</div>

  <div class="avatar" role="img" aria-label="Portrait photo of client" style="left:213px;opacity:.7"></div>
  <div class="avatar" role="img" aria-label="Portrait photo of client" style="left:568px"></div>
  <div class="avatar" role="img" aria-label="Portrait photo of client" style="left:923px;opacity:.7"></div>
  <div class="person faded" style="left:80px">Owen Carlisle <span>- Ledgerway</span></div>
  <div class="person" style="left:436px;color:var(--ink)">Neil Dorrance <span>- Corvane Finance Ceo</span></div>
  <div class="person faded" style="left:790px">Simon Hartley <span>- Tallis Consulting</span></div>
  <div class="stars faded" style="left:80px">★★★★★</div>
  <div class="stars" style="left:436px">★★★★★</div>
  <div class="stars faded" style="left:790px">★★★★★</div>
</section>

<footer class="footer">
  <h4 style="left:95px">CONTACTS</h4>
  <h4 style="left:395px">QUICK LINKS</h4>
  <h4 style="left:615px">NEWSLETTER</h4>
  <h4 style="left:925px">FOLLOW US</h4>
  <svg class="abs" style="left:95px;top:96px" width="10" height="14" viewBox="0 0 26 36"><path d="M13 0a13 13 0 0 0-13 13c0 9 13 23 13 23s13-14 13-23A13 13 0 0 0 13 0z" fill="#fff"/><circle cx="13" cy="13" r="5" fill="var(--navy)"/></svg>
  <div class="abs" style="left:122px;top:92px;font-size:12px;font-weight:600">42 Harlow Lane, Suite B<br>Marlow Park, New Jersey 07099</div>
  <svg class="abs" style="left:95px;top:168px" width="13" height="13" viewBox="0 0 24 24"><path fill="#fff" d="M6.6 10.8a15 15 0 0 0 6.6 6.6l2.2-2.2c.3-.3.7-.4 1-.2 1.1.4 2.3.6 3.6.6.6 0 1 .4 1 1V20c0 .6-.4 1-1 1A17 17 0 0 1 3 4c0-.6.4-1 1-1h3.5c.6 0 1 .4 1 1 0 1.3.2 2.5.6 3.6.1.3 0 .7-.2 1z"/></svg>
  <div class="abs" style="left:130px;top:165px;font-size:12px;font-weight:600">+ 0400 555 182</div>
  <svg class="abs" style="left:95px;top:218px" width="14" height="13" viewBox="0 0 24 22"><rect x="5" y="0" width="14" height="6" fill="#fff"/><rect x="0" y="7" width="24" height="10" rx="2" fill="#fff"/><rect x="5" y="14" width="14" height="8" fill="#fff" stroke="var(--navy)" stroke-width="2"/></svg>
  <div class="abs" style="left:130px;top:215px;font-size:12px;font-weight:600">(03) 5550 2817</div>
  <div class="abs links"><span class="cur">Home</span><br>About<br>Service<br>Property Advice<br>Contact</div>
  <div class="abs newsletter">Enter your e-mail and subscribe to our newsletter</div>
  <input type="text" value="E - mail" aria-label="E-mail">
  <div class="btn">SUBSCRIBE</div>
  <div class="abs follow" aria-label="Social links"><span></span><span></span><span></span><span></span><span></span><span></span></div>
</footer>
<div class="abs copyright" style="left:0;width:1200px">Copyright © . All Rights Reserved</div>

</body>
</html>
```